New Business Cards for Torvin Group

We need a new Business Card to compliment our new logo. We are a vibrant design, manufacture and install business providing recreation areas, public parks and Municipal spaces. We want business cards that are classy, modern and clean.

We have recently changed our logo, and are celebrating our 40th anniversary. We want business cards with a new modern design to reflect our status.

Target Market(s)

Customers

Contact Information for Business Card

We need all the details of our 3 offices as per the business card attached. Please disregard the old logo on the business card, the other three files show our new logo.

Requirements
Must have
• All info as per attached business card but with new logo.
Nice to have

```html
<!DOCTYPE html>
<html lang="en">
<head>
<meta charset="utf-8">
<title>Torvin Group Business Card</title>
<link href="https://fonts.googleapis.com/css2?family=Open+Sans:wght@400;600;700&display=swap" rel="stylesheet">
<style>
  :root {
    --backdrop: #e07173;
    --card: #f7f7f7;
    --brand-red: #e8262b;
    --ink: #1d1d1f;
    --ink-soft: #6b6b6e;
    --charcoal: #3d3d40;
  }
  * { box-sizing: border-box; margin: 0; padding: 0; }
  html, body { width: 1200px; height: 857px; overflow: hidden; }
  body {
    background: var(--backdrop);
    font-family: "Open Sans", Arial, sans-serif;
    color: var(--ink);
    position: relative;
  }
  .card {
    position: absolute;
    top: 285px;
    width: 500px;
    height: 286px;
    background: var(--card);
    box-shadow: 0 12px 30px rgba(0,0,0,.25);
    overflow: hidden;
  }
  .card--front { left: 60px; }
  .card--back { left: 640px; }
  .card__band {
    position: absolute;
    left: 0; right: 0; bottom: 0;
    height: 34px;
    background: var(--brand-red);
    color: #fff;
    font-size: 12px;
    font-weight: 600;
    display: flex;
    align-items: center;
    padding-left: 26px;
  }
  .brand {
    position: absolute;
    display: flex;
    align-items: center;
    gap: 10px;
    color: var(--charcoal);
    font-weight: 700;
    white-space: nowrap;
  }
  .brand__dot { border-radius: 50%; background: var(--brand-red); flex: none; }
  .card--front .brand { left: 26px; top: 104px; font-size: 34px; }
  .card--front .brand__dot { width: 30px; height: 30px; }
  .card--back .brand { left: 170px; top: 116px; font-size: 20px; }
  .card--back .brand__dot { width: 18px; height: 18px; }
  .person {
    position: absolute;
    right: 24px;
    top: 28px;
    text-align: right;
  }
  .person__name { font-size: 20px; font-weight: 400; }
  .person__role { font-size: 13px; color: var(--ink-soft); margin-top: 2px; }
  .person__contact { font-size: 10.5px; line-height: 1.55; margin-top: 14px; }
  .office { position: absolute; font-size: 8.5px; line-height: 1.45; }
  .office__title { font-size: 11px; font-weight: 700; }
  .office--head { right: 22px; top: 22px; text-align: right; font-size: 10px; }
  .office--head .office__title { font-size: 13px; }
  .office--dubai { left: 22px; top: 20px; }
  .office--qatar { right: 22px; bottom: 50px; text-align: right; }
</style>
</head>
<body>
  <section class="card card--front" aria-label="Business card front">
    <div class="brand"><span class="brand__dot"></span>Torvin Group</div>
    <div class="person">
      <p class="person__name">Marek Halloran</p>
      <p class="person__role">Managing Partner</p>
      <p class="person__contact">Mobile No.: +971 (0)50 418 7720<br>Email: marek@torvingroup.com</p>
    </div>
    <div class="card__band">www.torvingroup.com</div>
  </section>

  <section class="card card--back" aria-label="Business card back">
    <div class="office office--dubai">
      <p class="office__title">Dubai Office</p>
      <p>P.O.Box : 207415 Dubai, U.A.E.</p>
      <p>Tel No.: +971 (0)4 3086142</p>
      <p>Fax No.: +971 (0)4 3086143</p>
    </div>
    <div class="office office--head">
      <p class="office__title">Head Office</p>
      <p>P.O.Box : 31840 Abu Dhabi, U.A.E.</p>
      <p>Tel No.: +971 (0)2 5518290</p>
      <p>Fax No.: +971 (0)2 5518291</p>
    </div>
    <div class="brand"><span class="brand__dot"></span>Torvin Group</div>
    <div class="office office--qatar">
      <p class="office__title">Qatar Office</p>
      <p>P.O.Box : 22739 Doha, Qatar</p>
      <p>Tel No.: +974 44715308</p>
      <p>Fax No.: +974 44715309</p>
    </div>
    <div class="card__band">Email: sales@torvingroup.com</div>
  </section>
</body>
</html>
```